Powerpoint visual improvements

I need a cover page, and our beliefs page and differentiating factors page / graphic design for our presentation. For the cover page I would just like an attractive design that incorporate our architectural concept with columns and potentially our logo. For the beliefs page I just want a more attractive presentatoin of the concepts. For the differentiating factors page I want a graphic that captures the points about how we are different from competitors. I have used the attached content to date, but I think it can be improved. The text is included in the graphic and I would also like to make sure the firm logo is incorporated.

Target Market(s)

Individual and institutional investors.

Industry/Entity Type

Investment Advisory

Requirements
Must have
• Our corporate colors are generally RGB 145,148,149; 66,68,76; 0,0,153; and 0,63,127. Our logo is attached. Our primary font is Georgia. Our website is www.PelmarCW.com. The key pages are www.PelmarCW.com/beliefs and www.PelmarCW.com/value we are trying to capture in a presentation. We also need a new presentation cover. Use the website as a reference for the type of imagery we like.

```html
<!DOCTYPE html>
<html lang="en">
<head>
<meta charset="utf-8">
<title>Pelmar Capital Wealth – Presentation Slides</title>
<link href="https://fonts.googleapis.com/css2?family=Gelasio:wght@400;700&display=swap" rel="stylesheet">
<style>
  :root {
    --brand-gray: rgb(145,148,149);
    --brand-charcoal: rgb(66,68,76);
    --brand-navy: rgb(0,0,153);
    --brand-blue: rgb(0,63,127);
    --page-bg: #ffffff;
    --heading-gray: #6d7077;
    --body-gray: #6a6c72;
    --white: #ffffff;
  }
  * { box-sizing: border-box; margin: 0; padding: 0; }
  html, body {
    width: 1200px; height: 3000px; overflow: hidden;
    background: var(--page-bg);
    font-family: "Gelasio", Georgia, serif;
  }
  .canvas { position: relative; width: 1200px; height: 3000px; }
  .slide {
    position: absolute; left: 244px; width: 714px; height: 402px;
    overflow: hidden;
    box-shadow: 0 3px 10px rgba(0,0,0,0.35);
  }
  .slide--1 { top: 16px; } .slide--2 { top: 444px; } .slide--3 { top: 870px; }
  .slide--4 { top: 1300px; } .slide--5 { top: 1726px; } .slide--6 { top: 2154px; }
  .slide--7 { top: 2580px; }

  /* Cover slides */
  .cover-photo { position: absolute; inset: 0; }
  .cover-photo--cool { background: linear-gradient(160deg, #8d8e91 0%, #6b6c70 45%, #55565a 100%); }
  .cover-photo--warm { background: linear-gradient(150deg, #9b9a97 0%, #7f7e7c 50%, #6a6a6c 100%); }
  .cover-photo--hall { background: linear-gradient(180deg, #a4a5a8 0%, #8a8b8e 55%, #6f7073 100%); }
  .cover-window { position: absolute; border-radius: 50%; }
  .cover-window--grey { background: radial-gradient(circle at 40% 40%, #a9aaad 0%, #8a8b8e 60%, #6e6f72 100%); }
  .cover-window--gold { background: radial-gradient(circle at 45% 45%, #d8c9a8 0%, #a89676 45%, #6e6556 100%); }
  .cover-window--stone { background: radial-gradient(circle at 55% 40%, #b9bbbe 0%, #8e9093 55%, #5e6064 100%); }
  .cover-title {
    position: absolute; color: var(--white);
    font-size: 34px; font-weight: 400; line-height: 1; white-space: nowrap;
  }
  .cover-subtitle {
    position: absolute; color: var(--white);
    font-size: 11px; line-height: 1; white-space: nowrap;
  }
  .brand-mark { position: absolute; display: flex; align-items: center; gap: 8px; }
  .brand-mark__dot { width: 34px; height: 34px; border-radius: 50%; background: var(--white); }
  .brand-mark__name { color: var(--white); font-size: 22px; font-weight: 400; line-height: 1; }

  /* Content slides */
  .content-bg {
    position: absolute; inset: 0;
    background: linear-gradient(90deg, #eceef0 0%, #f7f8f9 20%, #e9ebed 38%, #f8f9fa 60%, #eaecee 80%, #f5f6f7 100%);
  }
  .slide-heading {
    position: absolute; left: 28px; top: 26px;
    color: var(--heading-gray); font-size: 25px; font-weight: 400;
  }
  .slide-heading__rule {
    position: absolute; left: 28px; top: 64px; width: 30px; height: 2px;
    background: var(--brand-charcoal);
  }
  .wheel { position: absolute; left: 210px; top: 50px; width: 300px; height: 300px; overflow: visible; }
  .connectors { position: absolute; inset: 0; width: 714px; height: 402px; }
  .point { position: absolute; font-size: 8.5px; line-height: 1.3; color: var(--body-gray); }
  .point--left { left: 28px; width: 172px; text-align: right; }
  .point__title { display: block; font-size: 10.5px; font-weight: 700; color: var(--brand-charcoal); margin-bottom: 2px; }
  .point__title--navy { color: var(--brand-navy); }
  .point__title--blue { color: var(--brand-blue); }
  .slide-footer {
    position: absolute; left: 0; right: 0; bottom: 0; height: 22px;
    background: linear-gradient(90deg, #a7aaab 0%, var(--brand-gray) 100%);
    display: flex; align-items: center;
  }
  .slide-footer__brand { display: flex; align-items: center; gap: 4px; margin-left: 10px; }
  .slide-footer__dot { width: 10px; height: 10px; border-radius: 50%; background: var(--white); }
  .slide-footer__name { color: var(--white); font-size: 8px; }
  .slide-footer__tagline { position: absolute; left: 334px; color: var(--white); font-size: 10px; }
  .slide-footer__page {
    position: absolute; right: 0; top: 0; width: 34px; height: 22px;
    background: var(--brand-charcoal); color: var(--white);
    font-size: 9px; display: flex; align-items: center; justify-content: center;
  }
  .seg-navy { fill: var(--brand-navy); stroke: var(--brand-navy); }
  .seg-blue { fill: var(--brand-blue); stroke: var(--brand-blue); }
  .seg-charcoal { fill: var(--brand-charcoal); stroke: var(--brand-charcoal); }
  .seg-gray { fill: #7d8087; stroke: #7d8087; }
  .seg-gray-light { fill: var(--brand-gray); stroke: var(--brand-gray); }
  .segment { stroke-width: 6; stroke-linejoin: round; }
  .icon { fill: none; stroke: var(--white); stroke-width: 2.2; stroke-linecap: round; stroke-linejoin: round; }
  .icon-fill { fill: var(--white); }
  .seg-label { fill: var(--white); font-family: "Gelasio", Georgia, serif; font-size: 7.5px; font-weight: 700; text-anchor: middle; }
  .connector { stroke: #8d9096; stroke-width: 0.8; }
  .connector-dot { fill: #8d9096; }
</style>
</head>
<body>
<div class="canvas">

  <!-- Cover 1 -->
  <section class="slide slide--1">
    <div class="cover-photo cover-photo--cool" role="img" aria-label="Photograph of a colonnade with long column shadows on the floor"></div>
    <div class="cover-window cover-window--grey" style="left:-54px; top:-16px; width:380px; height:380px;" role="img" aria-label="Circular inset photograph of stone columns"></div>
    <div class="brand-mark" style="left:562px; top:48px;"><span class="brand-mark__dot"></span><span class="brand-mark__name">Pelmar</span></div>
    <h1 class="cover-title" style="left:346px; top:288px;">Your Title Goes Here</h1>
    <p class="cover-subtitle" style="left:566px; top:332px;">Your Subtitle Goes Here</p>
  </section>

  <!-- Cover 2 -->
  <section class="slide slide--2">
    <div class="cover-photo cover-photo--warm" role="img" aria-label="Photograph of a row of classical columns in soft light"></div>
    <div class="cover-window cover-window--gold" style="left:-14px; top:-24px; width:360px; height:360px;" role="img" aria-label="Circular inset photograph of warm lit column bases"></div>
    <div class="brand-mark" style="left:562px; top:48px;"><span class="brand-mark__dot"></span><span class="brand-mark__name">Pelmar</span></div>
    <h1 class="cover-title" style="left:346px; top:288px;">Your Title Goes Here</h1>
    <p class="cover-subtitle" style="left:566px; top:332px;">Your Subtitle Goes Here</p>
  </section>

  <!-- Cover 3 -->
  <section class="slide slide--3">
    <div class="cover-photo cover-photo--cool" role="img" aria-label="Photograph of a long colonnade corridor"></div>
    <div class="cover-window cover-window--gold" style="left:366px; top:-20px; width:380px; height:380px;" role="img" aria-label="Circular inset photograph of sunlit columns casting striped shadows"></div>
    <div class="brand-mark" style="left:36px; top:44px;"><span class="brand-mark__dot"></span><span class="brand-mark__name">Pelmar</span></div>
    <h1 class="cover-title" style="left:48px; top:248px;">Your Title Goes Here</h1>
    <p class="cover-subtitle" style="left:254px; top:286px;">Your Subtitle Goes Here</p>
  </section>

  <!-- Cover 4 -->
  <section class="slide slide--4">
    <div class="cover-photo cover-photo--hall" role="img" aria-label="Photograph of a pale columned hall with reflective floor"></div>
    <div class="cover-window cover-window--stone" style="left:356px; top:20px; width:400px; height:400px;" role="img" aria-label="Circular inset photograph of grey stone columns"></div>
    <div class="brand-mark" style="left:36px; top:44px;"><span class="brand-mark__dot"></span><span class="brand-mark__name">Pelmar</span></div>
    <h1 class="cover-title" style="left:36px; top:280px;">Your Title Goes Here</h1>
    <p class="cover-subtitle" style="left:36px; top:320px;">Your Subtitle Goes Here</p>
  </section>

  <!-- The Difference, icon version -->
  <section class="slide slide--5">
    <div class="content-bg" role="img" aria-label="Faint pale photograph of white columns"></div>
    <h2 class="slide-heading">The Pelmar Difference</h2>
    <span class="slide-heading__rule"></span>
    <svg class="connectors" viewBox="0 0 714 402" aria-hidden="true">
      <line class="connector" x1="400" y1="82" x2="510" y2="82"/><circle class="connector-dot" cx="400" cy="82" r="2"/>
      <line class="connector" x1="484" y1="210" x2="530" y2="210"/><circle class="connector-dot" cx="484" cy="210" r="2"/>
      <line class="connector" x1="444" y1="318" x2="500" y2="318"/><circle class="connector-dot" cx="444" cy="318" r="2"/>
      <line class="connector" x1="204" y1="172" x2="262" y2="172"/><circle class="connector-dot" cx="262" cy="172" r="2"/>
      <line class="connector" x1="204" y1="296" x2="300" y2="296"/><circle class="connector-dot" cx="300" cy="296" r="2"/>
    </svg>
    <svg class="wheel" viewBox="-150 -150 300 300" aria-label="Five part wheel of differentiators">
      <path class="segment seg-navy" d="M -74.2 -118.7 A 140 140 0 0 1 74.2 -118.7 L 42.4 -67.8 A 80 80 0 0 0 -42.4 -67.8 Z"/>
      <path class="segment seg-blue" transform="rotate(72)" d="M -74.2 -118.7 A 140 140 0 0 1 74.2 -118.7 L 42.4 -67.8 A 80 80 0 0 0 -42.4 -67.8 Z"/>
      <path class="segment seg-charcoal" transform="rotate(144)" d="M -74.2 -118.7 A 140 140 0 0 1 74.2 -118.7 L 42.4 -67.8 A 80 80 0 0 0 -42.4 -67.8 Z"/>
      <path class="segment seg-gray" transform="rotate(216)" d="M -74.2 -118.7 A 140 140 0 0 1 74.2 -118.7 L 42.4 -67.8 A 80 80 0 0 0 -42.4 -67.8 Z"/>
      <path class="segment seg-gray-light" transform="rotate(288)" d="M -74.2 -118.7 A 140 140 0 0 1 74.2 -118.7 L 42.4 -67.8 A 80 80 0 0 0 -42.4 -67.8 Z"/>
      <circle cx="0" cy="0" r="66" fill="#ffffff"/>
      <circle cx="0" cy="0" r="50" fill="#dfe1e3"/>
      <circle cx="0" cy="0" r="36" fill="#b3b6b9"/>
      <g transform="translate(0,-108)"><circle class="icon" cx="0" cy="-2" r="8"/><path class="icon" d="M -4 -2 L -1 1 L 5 -5"/><path class="icon" d="M -5 6 L -7 13 M 5 6 L 7 13"/></g>
      <g transform="translate(104,-34)"><rect class="icon" x="-9" y="-11" width="14" height="18" rx="1.5"/><path class="icon" d="M -5 -5 H 1 M -5 -1 H 1"/><circle class="icon" cx="5" cy="6" r="4"/><path class="icon" d="M 8 9 L 11 12"/></g>
      <g transform="translate(64,89)"><circle class="icon" r="10"/><ellipse class="icon" rx="4.5" ry="10"/><path class="icon" d="M -10 0 H 10"/></g>
      <g transform="translate(-64,89)"><circle class="icon" r="10"/><circle class="icon" r="5"/><circle class="icon-fill" r="1.8"/></g>
      <g transform="translate(-104,-34)"><rect class="icon" x="-11" y="-9" width="13" height="9" rx="3"/><rect class="icon" x="-1" y="-2" width="13" height="9" rx="3"/></g>
    </svg>
    <p class="point" style="left:514px; top:66px; width:180px;"><span class="point__title point__title--navy">Experience Investors</span>Lorem Ipsum is simply dummy text of the printing and typesetting industry. Lorem Ipsum has been the industry's standard dummy text ever since the 1500s, when an unknown printer.</p>
    <p class="point" style="left:534px; top:196px; width:164px;"><span class="point__title point__title--blue">Institutional Research Process</span>Lorem Ipsum is simply dummy text of the printing and typesetting industry. Lorem Ipsum has been the industry's standard dummy text ever since the 1500s, when an unknown.</p>
    <p class="point" style="left:504px; top:308px; width:190px;"><span class="point__title">Proactive Total Fee Management</span>Lorem Ipsum is simply dummy text of the printing and typesetting industry. Lorem Ipsum has been the industry's standard dummy text ever since the 1500s, when an unknown.</p>
    <p class="point point--left" style="top:150px;"><span class="point__title">Transparent Communication</span>Lorem Ipsum is simply dummy text of the printing and typesetting industry. Lorem Ipsum has been the industry's standard dummy text ever since the 1500s, when an unknown.</p>
    <p class="point point--left" style="top:274px;"><span class="point__title">Sound Operational Platform</span>Lorem Ipsum is simply dummy text of the printing and typesetting industry. Lorem Ipsum has been the industry's standard dummy text ever since the 1500s, when an unknown.</p>
    <footer class="slide-footer">
      <span class="slide-footer__brand"><span class="slide-footer__dot"></span><span class="slide-footer__name">Pelmar</span></span>
      <span class="slide-footer__tagline">Pelmar Capital Wealth is an investment advisor founded by investors.</span>
      <span class="slide-footer__page">3</span>
    </footer>
  </section>

  <!-- The Difference, labelled version -->
  <section class="slide slide--6">
    <div class="content-bg" role="img" aria-label="Faint pale photograph of white columns"></div>
    <h2 class="slide-heading">The Pelmar Difference</h2>
    <span class="slide-heading__rule"></span>
    <svg class="connectors" viewBox="0 0 714 402" aria-hidden="true">
      <line class="connector" x1="400" y1="84" x2="510" y2="84"/><circle class="connector-dot" cx="400" cy="84" r="2"/>
      <line class="connector" x1="484" y1="212" x2="530" y2="212"/><circle class="connector-dot" cx="484" cy="212" r="2"/>
      <line class="connector" x1="444" y1="320" x2="500" y2="320"/><circle class="connector-dot" cx="444" cy="320" r="2"/>
      <line class="connector" x1="204" y1="180" x2="262" y2="180"/><circle class="connector-dot" cx="262" cy="180" r="2"/>
      <line class="connector" x1="204" y1="296" x2="300" y2="296"/><circle class="connector-dot" cx="300" cy="296" r="2"/>
    </svg>
    <svg class="wheel" viewBox="-150 -150 300 300" aria-label="Five part wheel of differentiators">
      <path class="segment seg-navy" d="M -74.2 -118.7 A 140 140 0 0 1 74.2 -118.7 L 42.4 -67.8 A 80 80 0 0 0 -42.4 -67.8 Z"/>
      <path class="segment seg-blue" transform="rotate(72)" d="M -74.2 -118.7 A 140 140 0 0 1 74.2 -118.7 L 42.4 -67.8 A 80 80 0 0 0 -42.4 -67.8 Z"/>
      <path class="segment seg-charcoal" transform="rotate(144)" d="M -74.2 -118.7 A 140 140 0 0 1 74.2 -118.7 L 42.4 -67.8 A 80 80 0 0 0 -42.4 -67.8 Z"/>
      <path class="segment seg-gray" transform="rotate(216)" d="M -74.2 -118.7 A 140 140 0 0 1 74.2 -118.7 L 42.4 -67.8 A 80 80 0 0 0 -42.4 -67.8 Z"/>
      <path class="segment seg-gray-light" transform="rotate(288)" d="M -74.2 -118.7 A 140 140 0 0 1 74.2 -118.7 L 42.4 -67.8 A 80 80 0 0 0 -42.4 -67.8 Z"/>
      <circle cx="0" cy="0" r="66" fill="#ffffff"/>
      <circle cx="0" cy="0" r="50" fill="#dfe1e3"/>
      <circle cx="0" cy="0" r="36" fill="#b3b6b9"/>
      <text class="seg-label" x="0" y="-110"><tspan x="0">Experience</tspan><tspan x="0" dy="10">Investors</tspan></text>
      <text class="seg-label" x="106" y="-46"><tspan x="106">Institutional</tspan><tspan x="106" dy="10">Research</tspan><tspan x="106" dy="10">Process</tspan></text>
      <text class="seg-label" x="66" y="88"><tspan x="66">Proactive Total Fee</tspan><tspan x="66" dy="10">Management</tspan></text>
      <text class="seg-label" x="-66" y="88"><tspan x="-66">Sound Operational</tspan><tspan x="-66" dy="10">Platform</tspan></text>
      <text class="seg-label" x="-106" y="-38"><tspan x="-106">Transparent</tspan><tspan x="-106" dy="10">Communication</tspan></text>
    </svg>
    <p class="point" style="left:514px; top:70px; width:180px;">Lorem Ipsum is simply dummy text of the printing and typesetting industry. Lorem Ipsum has been the industry's standard dummy text ever since the 1500s, when an unknown.</p>
    <p class="point" style="left:534px; top:200px; width:164px;">Lorem Ipsum is simply dummy text of the printing and typesetting industry. Lorem Ipsum has been the industry's standard dummy text ever since the 1500s, when an unknown.</p>
    <p class="point" style="left:504px; top:312px; width:190px;">Lorem Ipsum is simply dummy text of the printing and typesetting industry. Lorem Ipsum has been the industry's standard dummy text ever since the 1500s, when an unknown.</p>
    <p class="point point--left" style="top:162px;">Lorem Ipsum is simply dummy text of the printing and typesetting industry. Lorem Ipsum has been the industry's standard dummy text ever since the 1500s, when an unknown.</p>
    <p class="point point--left" style="top:280px;">Lorem Ipsum is simply dummy text of the printing and typesetting industry. Lorem Ipsum has been the industry's standard dummy text ever since the 1500s, when an unknown.</p>
    <footer class="slide-footer">
      <span class="slide-footer__brand"><span class="slide-footer__dot"></span><span class="slide-footer__name">Pelmar</span></span>
      <span class="slide-footer__tagline">Pelmar Capital Wealth is an investment advisor founded by investors.</span>
      <span class="slide-footer__page">4</span>
    </footer>
  </section>

  <!-- Our Beliefs -->
  <section class="slide slide--7">
    <div class="content-bg" role="img" aria-label="Faint pale photograph of white columns"></div>
    <h2 class="slide-heading">Our Beliefs</h2>
    <span class="slide-heading__rule"></span>
    <svg class="connectors" viewBox="0 0 714 402" aria-hidden="true">
      <line class="connector" x1="420" y1="80" x2="510" y2="80"/><circle class="connector-dot" cx="420" cy="80" r="2"/>
      <line class="connector" x1="496" y1="232" x2="536" y2="232"/><circle class="connector-dot" cx="496" cy="232" r="2"/>
      <line class="connector" x1="204" y1="306" x2="306" y2="306"/><circle class="connector-dot" cx="306" cy="306" r="2"/>
    </svg>
    <svg class="wheel" viewBox="-150 -150 300 300" aria-label="Four part wheel of beliefs">
      <path class="segment seg-navy" d="M -91.9 -105.7 A 140 140 0 0 1 91.9 -105.7 L 52.5 -60.4 A 80 80 0 0 0 -52.5 -60.4 Z"/>
      <path class="segment seg-blue" transform="rotate(90)" d="M -91.9 -105.7 A 140 140 0 0 1 91.9 -105.7 L 52.5 -60.4 A 80 80 0 0 0 -52.5 -60.4 Z"/>
      <path class="segment seg-charcoal" transform="rotate(180)" d="M -91.9 -105.7 A 140 140 0 0 1 91.9 -105.7 L 52.5 -60.4 A 80 80 0 0 0 -52.5 -60.4 Z"/>
      <path class="segment seg-gray-light" transform="rotate(270)" d="M -91.9 -105.7 A 140 140 0 0 1 91.9 -105.7 L 52.5 -60.4 A 80 80 0 0 0 -52.5 -60.4 Z"/>
      <circle cx="0" cy="0" r="66" fill="#ffffff"/>
      <circle cx="0" cy="0" r="50" fill="#dfe1e3"/>
      <circle cx="0" cy="0" r="36" fill="#b3b6b9"/>
      <g transform="translate(0,-108)"><circle class="icon" cx="0" cy="-3" r="6"/><circle class="icon-fill" cx="0" cy="-3" r="2"/><path class="icon" d="M -11 8 H 11"/><path class="icon" d="M -6 8 V 4 M 6 8 V 4"/></g>
      <g transform="translate(108,0)"><rect class="icon" x="-9" y="-11" width="14" height="18" rx="1.5"/><path class="icon" d="M -5 -5 H 1 M -5 -1 H 1"/><circle class="icon" cx="5" cy="6" r="4"/><path class="icon" d="M 8 9 L 11 12"/></g>
      <g transform="translate(0,108)"><path class="icon" d="M -10 -5 V -10 H -5 M 5 -10 H 10 V -5 M 10 5 V 10 H 5 M -5 10 H -10 V 5"/><circle class="icon" r="4"/></g>
      <g transform="translate(-108,0)"><circle class="icon" cx="-4" cy="0" r="6"/><path class="icon" d="M 2 0 H 12 M 8 0 V 5 M 11 0 V 4"/></g>
    </svg>
    <p class="point" style="left:514px; top:64px; width:176px;"><span class="point__title point__title--navy">Cost Matters</span>We believe the average investor pays too much for investment planning and portfolio advice. We also believe that costs quietly limit the potential for wealth compounding. Our fee schedule is designed to be below industry averages.</p>
    <p class="point" style="left:540px; top:216px; width:156px;"><span class="point__title point__title--blue">Research Matters</span>We believe that accountability and thorough, rigorous research is critical to generating consistent returns. Our founders average more than 25 years of investment experience and we conduct all of our research in house.</p>
    <p class="point point--left" style="top:130px;"><span class="point__title">Access Matters</span>We believe everyone should have access to an experienced investment professional and high quality asset management. Our account minimums, fees and portfolios reflect this conviction.</p>
    <p class="point point--left" style="top:276px;"><span class="point__title">Focus Matters</span>We believe the average investor pays too much for investment planning and portfolio advice. We also believe that costs quietly limit the potential for wealth compounding. Our fee schedule is designed to be below industry averages.</p>
    <footer class="slide-footer">
      <span class="slide-footer__brand"><span class="slide-footer__dot"></span><span class="slide-footer__name">Pelmar</span></span>
      <span class="slide-footer__tagline">Pelmar Capital Wealth is an investment advisor founded by investors.</span>
      <span class="slide-footer__page">7</span>
    </footer>
  </section>

</div>
</body>
</html>
```